LantrovaMD Biz Card

We need a business card design for a software firm servicing the medical arena. This will be a plastic card, translucent. I will upload our site beta for layout ideas. We will be utilizing clear/plastic business cards for printing.

Target Market(s)

Medical Providers

Industry/Entity Type

Information Technology

Contact Information for Business Card

Kurt Basford
Managing Director

4738 Hollis Creek Drive
3rd Floor
Brenton, OR 30857
kbasford@LantrovaMD.example
(800)555-0193 Toll Free
(541)555-0148 Mobile

Font styles to use
Serif
Sans Serif

Colors
0592cd
00a990
33b8a4
33a6d7

```html
<!DOCTYPE html>
<html lang="en">
<head>
<meta charset="utf-8">
<title>LantrovaMD Business Card</title>
<link rel="stylesheet" href="https://fonts.googleapis.com/css2?family=Arimo:wght@400;700&display=swap">
<style>
  :root {
    --stage: #2e2f31;
    --card-blue: #0d5a8c;
    --card-blue-deep: #0a4a75;
    --card-white: #ffffff;
    --card-mist: #eef0f2;
    --accent-green: #8cc63f;
    --text-light: #ffffff;
    --text-soft: #dbe7f0;
  }
  * { box-sizing: border-box; margin: 0; padding: 0; }
  html, body { width: 1200px; height: 997px; overflow: hidden; }
  body {
    background: var(--stage);
    font-family: "Arimo", Arial, sans-serif;
    position: relative;
  }
  .card {
    position: absolute;
    width: 560px;
    height: 320px;
    border-radius: 22px;
    overflow: hidden;
    box-shadow: 0 18px 40px rgba(0,0,0,.45);
  }
  /* Back of card */
  .card-back {
    left: 90px; top: 110px;
    background: linear-gradient(160deg, #13649b, var(--card-blue-deep));
    display: flex; align-items: center; justify-content: center;
  }
  .brand {
    display: flex; align-items: center; gap: 12px;
    font-weight: 700; letter-spacing: 1px;
  }
  .brand-dot {
    width: 26px; height: 26px; border-radius: 50%;
    background: var(--accent-green);
  }
  .card-back .brand { font-size: 40px; color: var(--text-light); }
  /* Front of card */
  .card-front {
    left: 540px; top: 470px;
    background: var(--card-blue);
  }
  .front-top {
    position: absolute; left: 0; top: 0; width: 100%; height: 150px;
    background: linear-gradient(180deg, var(--card-white), var(--card-mist));
    display: flex; align-items: center; justify-content: center;
  }
  .card-front .brand { font-size: 34px; color: var(--card-blue); }
  .front-rule {
    position: absolute; left: 0; top: 156px; width: 100%; height: 4px;
    background: var(--card-white);
  }
  .tab { position: absolute; left: 40px; top: 160px; }
  .person { position: absolute; left: 30px; top: 188px; }
  .person-name {
    color: var(--accent-green); font-weight: 700; font-size: 19px; letter-spacing: .5px;
  }
  .person-title { color: var(--text-light); font-size: 14px; margin-top: 3px; }
  .contacts {
    position: absolute; left: 30px; top: 238px;
    list-style: none; color: var(--text-soft); font-size: 15px;
  }
  .contacts li { display: flex; align-items: center; gap: 10px; height: 24px; }
  .contacts svg { width: 13px; height: 13px; fill: var(--accent-green); flex: none; }
  .office {
    position: absolute; right: 28px; top: 180px; text-align: right;
    color: var(--text-light); font-size: 14px; line-height: 1.35; font-style: normal;
  }
  .office-name { color: var(--accent-green); font-weight: 700; font-size: 16px; margin-bottom: 3px; }
</style>
</head>
<body>
  <section class="card card-back" aria-label="Card back">
    <div class="brand"><span class="brand-dot"></span>LantrovaMD</div>
  </section>

  <section class="card card-front" aria-label="Card front">
    <div class="front-top">
      <div class="brand"><span class="brand-dot"></span>LantrovaMD</div>
    </div>
    <div class="front-rule"></div>
    <svg class="tab" width="20" height="10" viewBox="0 0 20 10" aria-hidden="true">
      <polygon points="0,0 20,0 10,10" fill="#ffffff"/>
    </svg>

    <div class="person">
      <p class="person-name">KURT BASFORD</p>
      <p class="person-title">Managing Director</p>
    </div>

    <ul class="contacts">
      <li>
        <svg viewBox="0 0 16 16" aria-hidden="true"><path d="M8 1 1 7h2v8h4v-5h2v5h4V7h2z"/></svg>
        (800) 555-0193
      </li>
      <li>
        <svg viewBox="0 0 16 16" aria-hidden="true"><path d="M3 2c1-1 2-1 3 0l1.5 2.5c.5 1 0 1.7-.6 2.2.8 1.6 1.8 2.6 3.4 3.4.5-.6 1.2-1.1 2.2-.6L15 11c1 1 1 2 0 3-2 2-6 1-9.5-2.5S1 4 3 2z"/></svg>
        (541) 555-0148
      </li>
      <li>
        <svg viewBox="0 0 16 16" aria-hidden="true"><path d="M1 3h14v10H1z"/></svg>
        kbasford@LantrovaMD.example
      </li>
    </ul>

    <address class="office">
      <p class="office-name">LantrovaMD Pvt Ltd</p>
      <p>4738 Hollis Creek Drive, 3rd Floor</p>
      <p>Brenton, OR 30857</p>
    </address>
  </section>
</body>
</html>
```